WP website design (TOVI)

We need a wordpress design that will incorporate a professional color scheme with company logo in a clean layout. The design needs to consider that this will be developed on a responsive theme. Colors are undetermined - those that will complement the logo.
Client mentions liking plinmerbid.com for the layout and use of color. Possible but not necessary to have large slideshow element.

Industry/Entity Type

It Company

Font styles to use
Sans Serif

Colors

Designer to choose colors to be used in the design.

Requirements
Must have
• - Navigation: 1)Home 2) Auctions 3) Services 4) About Us 5) FAQs 6) References 7) Contact Us

Site will have slideshow, please use high-end stock real estate image initially. Header will have logo. Social icons (Facebook, Twitter, Youtube)

Widgets Include: Email signup form, Featured Auctions, Featured Video widget.

Footer will have contact info (below), site navigation, smaller company logo, affiliation logos (attached).

TOVI Auction Group
4275 Birch Vale Lane
Marlowe, KY 40617
1-800-419-BIDS (2437)
Ph. (270) 386-9041
Fx. (270) 386-1158
Nice to have
• - Site will have drop-down menus - please indicate the styling, for instance the dropdown menus 1) Live 2) Online 3) Past - under the 'Auctions' link

```html
<!DOCTYPE html>
<html lang="en">
<head>
<meta charset="utf-8">
<title>TOVI Auction Group</title>
<link rel="stylesheet" href="https://fonts.googleapis.com/css2?family=Open+Sans:wght@400;600;700&display=swap">
<style>
:root{
  --red:#d1121b;
  --charcoal:#3a3a3a;
  --nav:#4a4a4a;
  --nav-dark:#2f2f2f;
  --text:#555;
  --muted:#888;
  --line:#dcdcdc;
  --footer:#3b3b3b;
  --footer-bar:#262626;
  --white:#fff;
}
*{box-sizing:border-box;margin:0;padding:0}
html,body{width:861px;height:1200px;overflow:hidden}
body{font-family:"Open Sans",Arial,sans-serif;color:var(--text);background:#fff;font-size:9px;line-height:1.45;position:relative}
.wrap{position:absolute;left:35px;width:791px}

/* header */
.site-header{top:0;height:80px}
.brand{position:absolute;left:0;top:28px;font-size:18px;font-weight:600;color:var(--charcoal);white-space:nowrap}
.phone{position:absolute;right:0;top:26px;display:flex;align-items:center;gap:6px;font-size:19px;color:var(--charcoal)}
.phone svg{width:20px;height:20px}

/* nav */
.main-nav{top:80px;height:32px;background:linear-gradient(var(--nav),var(--nav-dark));display:flex;z-index:3}
.main-nav .home{width:40px;background:var(--red);display:flex;align-items:center;justify-content:center}
.main-nav a{color:#eee;font-size:10px;font-weight:600;text-decoration:none;display:flex;align-items:center;padding:0 20px;border-right:1px solid #555;letter-spacing:.3px}
.main-nav .right{margin-left:auto;border-left:1px solid #555}
.dropdown{position:absolute;left:75px;top:112px;width:70px;background:rgba(50,50,50,.92);z-index:4}
.dropdown span{display:block;color:#eee;font-size:9px;font-weight:600;padding:5px 10px;border-bottom:1px solid #555}
.dropdown .active{background:var(--red)}

/* slide */
.slide{top:112px;height:236px;border:4px solid #fff;box-shadow:0 2px 6px rgba(0,0,0,.25);background:linear-gradient(180deg,#b7c9d8 0%,#d7dfe4 35%,#a8a39a 58%,#6f7b4e 80%,#5e6a3e 100%)}
.dots{top:354px;display:flex;justify-content:center;gap:5px}
.dots i{width:6px;height:6px;border-radius:50%;background:#bbb}
.dots i.on{background:var(--red)}

/* columns */
.main{top:372px;width:478px}
.side{top:372px;left:530px;width:296px}
h2{font-size:14px;font-weight:600;color:var(--charcoal);margin-bottom:6px}
h2 em{font-style:normal;color:var(--red)}
.welcome p{font-size:8.5px;color:var(--muted)}
.more{display:block;text-align:right;color:var(--red);font-size:8px;font-weight:700;margin-top:4px}

.card{border:1px solid var(--line);background:#fff;box-shadow:0 3px 4px rgba(0,0,0,.12);padding:8px 10px;margin-bottom:14px;height:162px;position:relative}
.card h3{font-size:9px;font-weight:600;color:var(--charcoal);border-bottom:1px solid var(--line);padding-bottom:5px;margin-bottom:8px;text-transform:uppercase}
.thumb{position:absolute;left:10px;top:32px;width:110px;height:80px;background:linear-gradient(180deg,#9fb4c6,#c9cbc4 50%,#6c7a48)}
.links{position:absolute;left:10px;top:120px;display:flex;gap:12px;font-size:8px;color:var(--muted)}
.links span::before{content:"";display:inline-block;width:7px;height:7px;border:1px solid var(--muted);margin-right:3px;vertical-align:-1px}
.info{margin-left:122px;font-size:8px}
.info .kind{color:var(--red);font-weight:700;font-size:9px}
.info p{color:var(--muted);margin:2px 0 4px}
.info b{color:var(--charcoal)}
.bid{display:inline-block;margin-top:7px;background:var(--red);color:#fff;font-weight:700;font-size:8.5px;padding:6px 14px;border-radius:2px}

.search{display:flex;border:1px solid var(--line);margin-bottom:22px;height:24px}
.search .field{flex:1;background:#fff}
.search .btn{flex:none;background:var(--red);color:#fff;font-weight:700;font-size:8px;padding:0 12px;margin:3px;display:flex;align-items:center}
.video{height:160px;background:linear-gradient(180deg,#9aa6b1,#c2c0b5 50%,#6b7a4c);position:relative;margin-bottom:18px}
.video svg{position:absolute;left:128px;top:60px}
.testi{display:flex;gap:8px;margin-bottom:9px;font-size:7.5px;color:var(--muted)}
.testi i{flex:none;width:14px;height:14px;background:var(--line);border-radius:2px}
.testi b{display:block;color:var(--charcoal);font-weight:600}
.newsletter p{font-size:8px;color:var(--muted);margin-bottom:6px}
.newsletter .search{margin:0}

/* footer */
.site-footer{position:absolute;left:0;top:1040px;width:861px;height:160px;background:var(--footer);color:#ccc}
.footer-contact{position:absolute;left:35px;top:16px;font-size:8px;line-height:1.55}
.badges{position:absolute;left:300px;top:26px;display:flex;gap:26px}
.badges i{display:block;width:56px;height:46px;background:#6a6a6a;border-radius:4px}
.badges i.round{border-radius:50%;width:46px}
.footer-bar{position:absolute;left:0;bottom:0;width:100%;height:28px;background:var(--footer-bar);display:flex;align-items:center;padding:0 35px;font-size:7.5px;color:#999}
.follow{margin-left:auto;display:flex;align-items:center;gap:5px;color:#ddd;font-weight:600}
.follow i{width:13px;height:13px;border-radius:50%;background:#666}
</style>
</head>
<body>

<header class="wrap site-header">
  <div class="brand">TOVI Auction Group</div>
  <div class="phone">
    <svg viewBox="0 0 20 20"><rect width="20" height="20" rx="3" fill="#d1121b"/><path d="M6 4l3 3-1.5 2a8 8 0 0 0 3.5 3.5L13 11l3 3-2 2C9 16 4 11 4 6z" fill="#fff"/></svg>
    270-386-9041
  </div>
</header>

<nav class="wrap main-nav">
  <span class="home"><svg width="14" height="13" viewBox="0 0 14 13"><path d="M7 0l7 6h-2v7H9V9H5v4H2V6H0z" fill="#fff"/></svg></span>
  <a>AUCTIONS</a><a>SERVICES</a><a>ABOUT US</a><a>FAQs</a><a>REFERENCES</a><a class="right">CONTACT US</a>
</nav>
<div class="dropdown"><span class="active">LIVE</span><span>ONLINE</span><span>PAST</span></div>

<div class="wrap slide" role="img" aria-label="Large brick estate home with double garage and landscaped lawn"></div>
<div class="wrap dots"><i class="on"></i><i></i><i></i><i></i></div>

<main class="wrap main">
  <section class="welcome">
    <h2>Welcome to <em>TOVI Auction Group</em></h2>
    <p>Lorem ipsum dolor sit amet, consectetuer adipiscing elit, sed diam nonummy nibh euismod tincidunt ut laoreet dolore magna aliquam erat volutpat. Ut wisi enim ad minim veniam, quis nostrud exerci tation ullamcorper suscipit lobortis nisl ut aliquip ex ea commodo consequat. Duis autem vel eum iriure dolor in hendrerit in vulputate velit esse molestie consequat, vel illum dolore eu feugiat nulla facilisis at vero eros et accumsan.</p>
    <span class="more">Read More</span>
  </section>

  <h2 style="margin-top:4px">Featured Auctions</h2>

  <article class="card">
    <h3>Absolute Online Only Auction – Antiques &amp; Collections</h3>
    <div class="thumb" role="img" aria-label="Auction property photo"></div>
    <div class="links"><span>Details</span><span>Gallery</span></div>
    <div class="info">
      <div class="kind">Live Off-site Auction with Online bidding</div>
      <p>Lorem ipsum dolor sit amet, consectetuer adipiscing elit, sed diam nonummy nibh euismod ut laoreet dolore magna.</p>
      <div><b>Begins:</b> Tuesday, December 23, 2014 at 1:00 PM EST</div>
      <div><b>Location:</b> P.O. Box 00000 Ashbury, TN 24810</div>
      <span class="bid">Click here for online bidding</span>
    </div>
  </article>

  <article class="card">
    <h3>Absolute Online Only Auction – Antiques &amp; Collections</h3>
    <div class="thumb" role="img" aria-label="Auction property photo"></div>
    <div class="links"><span>Details</span><span>Gallery</span></div>
    <div class="info">
      <div class="kind">Live Off-site Auction with Online bidding</div>
      <p>Lorem ipsum dolor sit amet, consectetuer adipiscing elit, sed diam nonummy nibh euismod ut laoreet dolore magna.</p>
      <div><b>Begins:</b> Tuesday, December 23, 2014 at 1:00 PM EST</div>
      <div><b>Location:</b> P.O. Box 00000 Ashbury, TN 24810</div>
      <span class="bid">Click here for online bidding</span>
    </div>
  </article>

  <article class="card">
    <h3>Absolute Online Only Auction – Antiques &amp; Collections</h3>
    <div class="thumb" role="img" aria-label="Auction property photo"></div>
    <div class="links"><span>Details</span><span>Gallery</span></div>
    <div class="info">
      <div class="kind">Live Off-site Auction with Online bidding</div>
      <p>Lorem ipsum dolor sit amet, consectetuer adipiscing elit, sed diam nonummy nibh euismod ut laoreet dolore magna.</p>
      <div><b>Begins:</b> Tuesday, December 23, 2014 at 1:00 PM EST</div>
      <div><b>Location:</b> P.O. Box 00000 Ashbury, TN 24810</div>
      <span class="bid">Click here for online bidding</span>
    </div>
  </article>
</main>

<aside class="wrap side">
  <h2>Auction Search</h2>
  <div class="search"><span class="field"></span><span class="btn">GO</span></div>

  <h2>Featured Video</h2>
  <div class="video" role="img" aria-label="Video still of a large home with trees">
    <svg width="40" height="40" viewBox="0 0 40 40"><circle cx="20" cy="20" r="19" fill="rgba(209,18,27,.9)"/><path d="M16 12l12 8-12 8z" fill="#fff"/></svg>
  </div>

  <h2>Client Testimonials</h2>
  <div class="testi"><i></i><div>Lorem ipsum dolor sit amet, consectetuer adipiscing elit, sed diam nonummy nibh euismod tincidunt ut laoreet dolore magna aliquam erat volutpat.<b>– Lorem Ipsum, Client</b></div></div>
  <div class="testi"><i></i><div>Lorem ipsum dolor sit amet, consectetuer adipiscing elit, sed diam nonummy nibh euismod tincidunt ut laoreet dolore magna aliquam erat volutpat.<b>– Lorem Ipsum, Client</b></div></div>
  <div class="testi"><i></i><div>Lorem ipsum dolor sit amet, consectetuer adipiscing elit, sed diam nonummy nibh euismod tincidunt ut laoreet dolore magna aliquam erat volutpat.<b>– Lorem Ipsum, Client</b></div></div>

  <section class="newsletter" style="margin-top:18px">
    <h2>Newsletter Signup</h2>
    <p>Sign up for our free messages &amp; receive auction alerts</p>
    <div class="search"><span class="field"></span><span class="btn">GO</span></div>
  </section>
</aside>

<footer class="site-footer">
  <div class="footer-contact">
    TOVI Auction Group<br>
    4275 Birch Vale Lane<br>
    Marlowe, KY 40617<br><br>
    Toll Free: 1-800-419-BIDS (2437)<br>
    Ph. (270) 386-9041<br>
    Fx. (270) 386-1158
  </div>
  <div class="badges"><i></i><i class="round"></i><i></i><i class="round"></i><i></i></div>
  <div class="footer-bar">
    <span>Copyright © 2014, TOVI Auction Group. All Rights Reserved.</span>
    <span class="follow">Follow Us <i></i><i></i><i></i></span>
  </div>
</footer>

</body>
</html>
```